Ridgeway Builders, Inc. Concrete cutting special flyer , 10% off for new customers

Flyer to send to potential customers and business associates and general contractors - specializing in Concrete-Flatwork
Concrete Repair
Concrete Sidewalks
Patios & Driveways
Stoops, Porches And Staircase
Foundation Contractors--Concrete
Facade Restoration
Concrete
Patios
Driveways
Walkways
Commercial Concrete Work
Concrete Restoration
Building Alterations
Foundations - Concrete
Concrete Repairs
rbwxpo.com

Target Market(s)

Homeowners, business owners & general contractors

Industry/Entity Type

Construction

Font styles to use
Serif

Colors
FFC000
F8CF3A
FAE287
FDF2CF
FEFAEE
EB3D1F
EC4F4E
F09395
F8D3D4
FCEDEE

Requirements
Must have
• General Contracting, masonry - Must have Logo Please see list of services Ridgeway Builders NY, Inc., has to offer. Concrete-Flatwork Concrete Repair Concrete Sidewalks Patios & Driveways Stoops, Porches And Staircase Foundation Contractors--Concrete Facade Restoration Concrete Patios Driveways Walkways Commercial Concrete Work Concrete Restoration Building Alterations Foundations - Concrete Concrete Repairs
Nice to have
• List of services - Logo - Black & Gold with a bold color to stand out (preferably reds)

```html
<!DOCTYPE html>
<html lang="en">
<head>
<meta charset="utf-8">
<title>Ridgeway Builders NY, Inc. – 10% Off Flyer</title>
<link href="https://fonts.googleapis.com/css2?family=Oswald:wght@500;700&family=Roboto+Condensed:wght@500;700&display=swap" rel="stylesheet">
<style>
  :root {
    --page-bg: #d9d9d9;
    --paper: #ececea;
    --paper-shade: #dcdcd8;
    --ink: #2b2b2b;
    --brand-green: #3d5a2a;
    --brand-green-dark: #2f4820;
    --offer-red: #e02a1f;
    --white: #ffffff;
    --tape-yellow: #f2c21a;
    --hat-yellow: #ffc000;
    --wood: #a57a4c;
    --tool-blue: #2a5f8f;
    --tool-grey: #3a3d42;
    --protractor: #9ec7e4;
  }
  * { box-sizing: border-box; margin: 0; padding: 0; }
  html, body { width: 1200px; height: 2224px; overflow: hidden; }
  body { background: var(--page-bg); position: relative; }

  .flyer {
    position: absolute; left: 0; top: 323px;
    width: 1200px; height: 1578px; overflow: hidden;
    background: radial-gradient(ellipse at 50% 45%, var(--paper) 0%, var(--paper-shade) 100%);
  }
  .art { position: absolute; }
  .art--tape {
    left: -80px; top: 30px; width: 300px; height: 56px;
    background: linear-gradient(var(--tape-yellow), #d9a80f);
    transform: rotate(-45deg);
  }
  .art--drill {
    left: 890px; top: 470px; width: 290px; height: 380px;
    background: linear-gradient(160deg, var(--tool-blue) 0%, var(--tool-grey) 70%);
    border-radius: 40px 40px 30px 30px;
    opacity: .9;
  }
  .art--wood {
    left: 0; top: 1170px; width: 150px; height: 408px;
    background: linear-gradient(90deg, #8a6438, var(--wood), #c09a6a);
  }
  .art--protractor {
    left: 150px; top: 1330px; width: 250px; height: 150px;
    background: linear-gradient(var(--protractor), #c7e0f0);
    border-radius: 125px 125px 0 0; opacity: .8;
  }
  .art--hardhat {
    left: 880px; top: 1180px; width: 400px; height: 400px;
    background: radial-gradient(circle at 40% 35%, #ffd95a, var(--hat-yellow) 60%, #d99e00);
    border-radius: 50%;
  }

  .brand {
    position: absolute; left: 60px; top: 150px;
    display: flex; align-items: center; gap: 18px;
  }
  .brand__mark { width: 44px; height: 44px; background: var(--brand-green); }
  .brand__name {
    font-family: 'Oswald', sans-serif; font-weight: 700; color: var(--brand-green);
    font-size: 58px; line-height: 1; text-transform: uppercase; letter-spacing: 1px;
  }
  .brand__name small { display: block; font-size: 21px; letter-spacing: 3px; margin-top: 6px; }

  .offer { position: absolute; left: 408px; top: 72px; width: 762px; text-align: center; }
  .offer__badge {
    background: var(--offer-red); color: var(--white);
    font-family: 'Oswald', sans-serif; font-weight: 700;
    font-size: 118px; line-height: 156px; height: 156px;
  }
  .offer__note {
    color: var(--offer-red); font-family: 'Oswald', sans-serif; font-weight: 500;
    font-size: 66px; line-height: 90px; text-transform: uppercase;
  }

  .services__title {
    position: absolute; left: 100px; top: 360px;
    font-family: 'Oswald', sans-serif; font-weight: 700; font-size: 96px; line-height: 120px;
    color: var(--ink); letter-spacing: 2px;
  }
  .services__list {
    position: absolute; top: 498px; width: 360px; list-style: none;
    display: flex; flex-direction: column; gap: 30px;
  }
  .services__list--left { left: 108px; }
  .services__list--right { left: 498px; }
  .services__item {
    height: 66px; background: var(--brand-green); color: var(--white);
    font-family: 'Roboto Condensed', sans-serif; font-weight: 500; font-size: 26px;
    display: flex; align-items: center; justify-content: center;
    border-bottom: 4px solid var(--brand-green-dark);
  }

  .web {
    position: absolute; left: 0; right: 0; top: 1400px; text-align: center;
    font-family: 'Roboto Condensed', sans-serif; font-weight: 700; font-size: 32px;
    letter-spacing: 8px; color: var(--ink);
  }
</style>
</head>
<body>
  <main class="flyer">
    <div class="art art--tape" role="img" aria-label="Yellow measuring tape across the corner"></div>
    <div class="art art--drill" role="img" aria-label="Cordless power drill"></div>
    <div class="art art--wood" role="img" aria-label="Wood block with pencils"></div>
    <div class="art art--protractor" role="img" aria-label="Clear plastic protractor"></div>
    <div class="art art--hardhat" role="img" aria-label="Yellow safety hard hat"></div>

    <div class="brand">
      <span class="brand__mark"></span>
      <div class="brand__name">Ridgeway<small>Builders NY, Inc.</small></div>
    </div>

    <div class="offer">
      <div class="offer__badge">10% OFF</div>
      <div class="offer__note">For New Customers</div>
    </div>

    <h2 class="services__title">SERVICES</h2>
    <ul class="services__list services__list--left">
      <li class="services__item">Stoops, Porches, Staircase</li>
      <li class="services__item">Concrete Repairs</li>
      <li class="services__item">Building Alterations</li>
      <li class="services__item">Concrete Restoration</li>
      <li class="services__item">Foundation Concrete</li>
      <li class="services__item">Foundation Contractors</li>
      <li class="services__item">Commercial Concrete</li>
    </ul>
    <ul class="services__list services__list--right">
      <li class="services__item">Patios / Concrete</li>
      <li class="services__item">Driveways</li>
      <li class="services__item">Walkways</li>
      <li class="services__item">Concrete Repair</li>
      <li class="services__item">Concrete Sidewalks</li>
      <li class="services__item">Patios &amp; Driveways</li>
      <li class="services__item">Facade Restoration</li>
    </ul>

    <p class="web">WWW.RBWXPO.COM</p>
  </main>
</body>
</html>
```